New Web Design Project

New Roofing Website homepage mockup

Complete design document here: https://files.plenovark.com/document/d/7kRtWmZpQ2vLxB9nHcYdF4sJgTuEaOiMbNwXzCyVqhr/edit?usp=sharing
Updates

PROJECT IS NOW CLOSED. ANY NEW SUBMISSIONS WILL BE AUTO REJECTED

Number of Pages Required

1 page

Font styles to use
Sans Serif

```html
<!DOCTYPE html>
<html lang="en">
<head>
<meta charset="utf-8">
<title>Keystone Roofing — Built Right, Built To Last</title>
<link rel="stylesheet" href="https://fonts.googleapis.com/css2?family=Oswald:wght@400;500&family=Roboto:wght@300;400&display=swap">
<style>
:root{
  --blue:#1f9ad8;
  --blue-dark:#1479b2;
  --page:#f5f6f8;
  --band:#e8eaee;
  --ink:#1c1d1f;
  --muted:#7d8084;
  --slate:#3c3e42;
  --footer:#232427;
  --footer-text:#b9bcc1;
  --white:#ffffff;
}
*{margin:0;padding:0;box-sizing:border-box}
html,body{width:1200px;height:4902px;overflow:hidden;background:var(--page)}
body{position:relative;font-family:'Roboto',sans-serif;color:var(--ink)}
.abs{position:absolute}
.display{font-family:'Oswald',sans-serif;text-transform:uppercase;font-weight:500}
.photo{position:absolute;overflow:hidden}
.section-title{position:absolute;left:0;width:1200px;text-align:center;font-family:'Oswald',sans-serif;font-weight:500;font-size:44px;line-height:1;text-transform:uppercase;color:var(--ink)}
.title-rule{position:absolute;left:568px;width:64px;height:3px;background:var(--blue)}

/* hero */
.hero-photo{left:0;top:0;width:1200px;height:720px;background:linear-gradient(160deg,#4a5a4a 0%,#6f7873 30%,#9aa0a3 55%,#5d6a55 85%,#3f4d38 100%);clip-path:polygon(0 0,1200px 0,1200px 680px,0 692px)}
.hero-shade{left:0;top:0;width:1200px;height:720px;background:rgba(20,24,28,.25);clip-path:polygon(0 0,1200px 0,1200px 680px,0 692px)}
.brand{position:absolute;display:flex;align-items:center;gap:10px;font-family:'Oswald',sans-serif;font-weight:500;text-transform:uppercase;color:var(--white)}
.brand-mark{width:18px;height:18px;background:var(--white)}
.nav{left:485px;top:46px;display:flex;gap:0;font-family:'Oswald',sans-serif;font-size:15px;text-transform:uppercase;color:var(--white)}
.nav a{color:inherit;text-decoration:none;margin-right:28px}
.nav a.active{color:var(--blue)}
.hero-title{left:0;width:1200px;text-align:center;color:var(--white);line-height:1}
.btn{position:absolute;display:flex;align-items:center;justify-content:center;background:var(--blue);color:var(--white);font-family:'Oswald',sans-serif;font-size:15px;text-transform:uppercase;clip-path:polygon(0 0,100% 0,100% 70%,calc(100% - 16px) 100%,0 100%)}
.dots{left:36px;top:294px;display:flex;flex-direction:column;gap:9px}
.dots span{width:11px;height:11px;border:2px solid var(--white);border-radius:50%}
.dots span.on{background:var(--white)}

/* services */
.service-label{position:absolute;height:74px;background:var(--white);box-shadow:0 6px 14px rgba(0,0,0,.12);display:flex;align-items:center;justify-content:center;font-family:'Oswald',sans-serif;font-size:32px;text-transform:uppercase;color:#8a8d91;clip-path:polygon(0 0,100% 0,100% 62%,calc(100% - 28px) 100%,0 100%)}

/* about */
.about-band{left:0;top:1400px;width:1200px;height:865px;background:linear-gradient(180deg,#e4e7eb,#eef0f3)}
.about-heading{left:614px;top:1706px;font-family:'Oswald',sans-serif;font-size:38px;line-height:46px;text-transform:uppercase;color:var(--ink)}
.about-text{left:614px;top:1846px;width:496px;font-size:14px;line-height:22px;font-weight:300;color:var(--muted)}

/* roofs */
.roof{position:absolute;top:2420px;width:186px;height:186px;border-radius:50%;display:flex;align-items:flex-end;justify-content:center;padding-bottom:26px;font-family:'Oswald',sans-serif;font-weight:500;font-size:20px;text-transform:uppercase;color:var(--white)}
.divider{left:0;top:2696px;width:1200px;height:2px;background:#e3e5e8}

/* cta */
.cta-photo{left:0;top:3640px;width:1200px;height:400px;background:linear-gradient(180deg,#dfe2e6,#c9ced4 60%,#d9dde2)}
.cta-veil{left:0;top:3640px;width:1200px;height:400px;background:rgba(245,246,248,.7)}
.cta-text{left:0;top:3818px;width:1200px;text-align:center;font-size:14px;line-height:22px;font-weight:300;color:#55585c}

/* testimonial */
.quote{left:238px;top:4228px;width:772px;text-align:center;font-size:14px;line-height:22px;font-weight:300;color:var(--muted)}
.client-name{left:0;width:1200px;text-align:center;font-family:'Oswald',sans-serif;text-transform:uppercase}

/* footer */
.footer-bg{left:0;top:4440px;width:1200px;height:462px}
.f-head{font-family:'Oswald',sans-serif;font-size:16px;text-transform:uppercase;color:var(--white)}
.f-link{font-size:13px;color:var(--footer-text)}
.f-item{display:flex;align-items:center;gap:12px;font-size:13px;color:var(--footer-text)}
.f-icon{width:22px;height:22px;border-radius:50%;background:#3d3f43}
.f-rule{left:91px;top:4830px;width:1018px;height:1px;background:#3a3c40}
.copy{left:0;top:4860px;width:1200px;text-align:center;font-size:12px;color:var(--footer-text)}
</style>
</head>
<body>

<!-- HERO -->
<div class="photo hero-photo" role="img" aria-label="Aerial view of a large white house with a new dark shingle roof among trees"></div>
<div class="abs hero-shade"></div>
<svg class="abs" style="left:0;top:660px" width="1200" height="140" viewBox="0 0 1200 140">
  <polygon points="0,32 1200,20 1200,140 0,140" fill="var(--page)"/>
  <polygon points="470,52 1200,20 1200,125" fill="var(--blue)"/>
</svg>

<div class="brand" style="left:91px;top:58px;font-size:22px"><span class="brand-mark"></span>Keystone Roofing</div>
<nav class="abs nav">
  <a class="active">Home</a><a>About</a><a>Blog</a><a>Reviews</a><a>Services</a><a>Affiliations</a><a>Contact</a><a style="margin-right:0">Projects</a>
</nav>
<div class="abs dots"><span></span><span></span><span class="on"></span><span></span></div>

<div class="abs hero-title display" style="top:224px;font-size:76px">Built Right,</div>
<div class="abs hero-title display" style="top:308px;font-size:104px">Built To Last</div>
<div class="btn" style="left:485px;top:434px;width:230px;height:45px">Get An Instant Estimate</div>

<!-- SERVICES -->
<h2 class="section-title" style="top:858px">Our Services</h2>
<div class="title-rule" style="top:922px"></div>

<div class="photo" style="left:88px;top:964px;width:498px;height:292px;background:linear-gradient(135deg,#5b5f63,#8e949a 55%,#c9b06a)" role="img" aria-label="Roofer in hard hat and safety vest installing slate tiles"></div>
<div class="service-label" style="left:127px;top:1223px;width:419px">Roof Installation</div>
<div class="photo" style="left:609px;top:964px;width:500px;height:292px;background:linear-gradient(135deg,#3a4c6e,#5d4d48 50%,#2e7bc4)" role="img" aria-label="Roofer repairing dark clay roof tiles"></div>
<div class="service-label" style="left:650px;top:1223px;width:419px">Roof Repair</div>

<!-- ABOUT -->
<div class="abs about-band" role="img" aria-label="Faint background of roof tiles"></div>
<svg class="abs" style="left:0;top:1400px" width="1200" height="870" viewBox="0 0 1200 870">
  <polygon points="0,0 1200,66 0,100" fill="var(--slate)"/>
  <polygon points="0,66 1200,66 1200,100 0,100" fill="var(--page)" opacity="0"/>
  <polygon points="0,100 1200,66 1200,0 0,0" fill="none"/>
  <polygon points="0,760 1200,760 1200,870 0,870" fill="var(--page)" opacity="0"/>
  <polygon points="480,812 1200,760 1200,862" fill="var(--blue)"/>
  <polygon points="0,820 480,812 1200,862 1200,870 0,870" fill="var(--page)"/>
</svg>

<div class="photo" style="left:89px;top:1598px;width:377px;height:275px;background:linear-gradient(135deg,#4aa6d6,#b0705a 60%,#8c5a45)" role="img" aria-label="Roofer nailing red clay tiles"></div>
<div class="photo" style="left:466px;top:1651px;width:101px;height:222px;background:linear-gradient(180deg,#e2b532,#c9d52e 60%,#6c7a80)" role="img" aria-label="Worker in yellow hard hat and ear protection"></div>
<div class="photo" style="left:89px;top:1893px;width:181px;height:161px;background:linear-gradient(135deg,#4c5a6e,#b98c58)" role="img" aria-label="Roof rafters and tiles being laid"></div>
<div class="photo" style="left:293px;top:1893px;width:274px;height:161px;background:linear-gradient(135deg,#c8c4bc,#a79d8d)" role="img" aria-label="Gloved hand spreading mortar on tiles"></div>

<h2 class="abs about-heading">About Us<br>For Keystone Roofing</h2>
<div class="abs" style="left:614px;top:1805px;width:64px;height:3px;background:var(--blue)"></div>
<p class="abs about-text">After over a decade of general contracting, we continue to see a repetitive trend by the roof purchase process where homeowners are constantly left confused, nervous, and worried when they need a new roof. As one of the most important features of keeping your home safe, this is unacceptable. Keystone Roofing was created to break this trend.</p>

<!-- TYPES OF ROOFS -->
<h2 class="section-title" style="top:2308px">Types Of Roofs</h2>
<div class="title-rule" style="top:2372px"></div>
<div class="roof" style="left:92px;background:linear-gradient(160deg,#a08a72,#6e5a47)" role="img" aria-label="Cedar shake texture">Cedar</div>
<div class="roof" style="left:299px;background:radial-gradient(circle,#7a4a35,#3b2219)" role="img" aria-label="Copper metal scale texture">Metal</div>
<div class="roof" style="left:506px;background:linear-gradient(135deg,#5d646b,#2f3439)" role="img" aria-label="Grey slate tile texture">Slate</div>
<div class="roof" style="left:713px;background:radial-gradient(circle,#2a2a2a,#0d0d0d)" role="img" aria-label="Black asphalt shingle texture">Asphalt</div>
<div class="roof" style="left:919px;background:radial-gradient(circle,#3d4441,#1c201f)" role="img" aria-label="Dark rubber membrane texture">Rubber</div>
<div class="abs divider"></div>

<!-- RECENT PROJECTS -->
<h2 class="section-title" style="top:2787px">Recent Projects</h2>
<div class="title-rule" style="top:2852px"></div>
<div class="photo" style="left:89px;top:2891px;width:425px;height:278px;background:linear-gradient(180deg,#d6d9dc,#6d7277 55%,#2c2f33)" role="img" aria-label="Company pickup truck parked before a house"></div>
<div class="photo" style="left:533px;top:2891px;width:279px;height:278px;background:linear-gradient(180deg,#9ab8d6,#8e949a 45%,#7f8a6a)" role="img" aria-label="Grey shingled colonial home"></div>
<div class="photo" style="left:831px;top:2891px;width:278px;height:278px;background:linear-gradient(180deg,#5f8fc6,#9bb8d8 55%,#3b3f44)" role="img" aria-label="Cupola with weathervane on a roof"></div>
<div class="photo" style="left:89px;top:3190px;width:278px;height:277px;background:linear-gradient(180deg,#4e6b3c,#d9dadc 50%,#5c7a44)" role="img" aria-label="Aerial view of a white house with deck"></div>
<div class="photo" style="left:388px;top:3190px;width:278px;height:277px;background:linear-gradient(135deg,#5aa9d3,#2f7fb4)" role="img" aria-label="Curved eyebrow roof detail with blue siding">
  <svg style="position:absolute;left:117px;top:116px" width="44" height="44" viewBox="0 0 44 44"><rect x="19" y="0" width="6" height="44" fill="#fff"/><rect x="0" y="19" width="44" height="6" fill="#fff"/></svg>
</div>
<div class="photo" style="left:683px;top:3190px;width:424px;height:277px;background:linear-gradient(180deg,#4d6a3a,#c9cdd0 50%,#6a8150)" role="img" aria-label="Large white farmhouse with metal roof"></div>

<!-- CHOOSE ROOF TYPE -->
<div class="photo cta-photo" role="img" aria-label="Faded photo of a large home"></div>
<div class="abs cta-veil"></div>
<svg class="abs" style="left:0;top:3574px" width="1200" height="500" viewBox="0 0 1200 500">
  <polygon points="0,0 1200,66 1200,66 0,106" fill="var(--slate)"/>
  <polygon points="0,0 1200,0 1200,66" fill="var(--page)"/>
  <polygon points="480,442 1200,392 1200,496" fill="var(--blue)"/>
  <polygon points="0,440 480,442 1200,496 1200,500 0,500" fill="var(--page)"/>
</svg>
<h2 class="section-title" style="top:3722px">Choose Your Roof Type</h2>
<p class="abs cta-text">A roof does more than keep the rain off your head. It protects your biggest investment –<br>your home.</p>
<div class="btn" style="left:441px;top:3880px;width:316px;height:46px">Calculate The Cost Of A New Roof Now</div>

<!-- HAPPY CLIENTS -->
<h2 class="section-title" style="top:4121px">Happy Clients</h2>
<div class="title-rule" style="top:4185px"></div>
<svg class="abs" style="left:188px;top:4198px" width="46" height="34" viewBox="0 0 46 34"><circle cx="10" cy="12" r="10" fill="#cfe6f4"/><path d="M2 14 Q2 30 14 34 Q6 26 8 16Z" fill="#cfe6f4"/><circle cx="34" cy="12" r="10" fill="#cfe6f4"/><path d="M26 14 Q26 30 38 34 Q30 26 32 16Z" fill="#cfe6f4"/></svg>
<p class="abs quote">We needed to put a new roof on our house, as well as repair a sagging porch roof. Shingles had been flying off and we had had several leaks. Dana provided a very reasonable estimate - well below some of the other HomePro Finder companies. The work was done very promptly and professionally. A couple of issues that arose were settled to our satisfaction and Dana took full ownership of the situation. It was very clear that customer satisfaction is a priority for this company. I would definitely recommend and hire again.</p>
<svg class="abs" style="left:740px;top:4338px" width="46" height="34" viewBox="0 0 46 34"><g transform="rotate(180 23 17)"><circle cx="10" cy="12" r="10" fill="#cfe6f4"/><path d="M2 14 Q2 30 14 34 Q6 26 8 16Z" fill="#cfe6f4"/><circle cx="34" cy="12" r="10" fill="#cfe6f4"/><path d="M26 14 Q26 30 38 34 Q30 26 32 16Z" fill="#cfe6f4"/></g></svg>
<div class="abs client-name" style="top:4352px;font-size:20px;color:var(--blue);font-weight:400">Owen</div>
<div class="abs client-name" style="top:4380px;font-size:20px;color:var(--ink)">Brookfield, MA</div>

<!-- FOOTER -->
<svg class="abs footer-bg" width="1200" height="462" viewBox="0 0 1200 462">
  <polygon points="0,0 1200,110 1200,462 0,462" fill="var(--slate)"/>
  <polygon points="0,110 1200,70 1200,462 0,462" fill="var(--footer)"/>
</svg>

<div class="brand" style="left:91px;top:4676px;font-size:34px"><span class="brand-mark" style="width:26px;height:26px"></span>Keystone Roofing</div>

<div class="abs f-head" style="left:418px;top:4612px">Quick Links</div>
<div class="abs f-link" style="left:418px;top:4654px;line-height:35px">› Home<br>› About<br>› Blog<br>› Reviews</div>
<div class="abs f-link" style="left:513px;top:4654px;line-height:35px">› Services<br>› Affiliations<br>› Contact<br>› Projects</div>

<div class="abs f-head" style="left:668px;top:4612px">Connect With</div>
<div class="abs" style="left:668px;top:4652px;display:flex;flex-direction:column;gap:13px">
  <div class="f-item"><span class="f-icon"></span>Friendbook</div>
  <div class="f-item"><span class="f-icon"></span>Chirper</div>
  <div class="f-item"><span class="f-icon"></span>Snapgram</div>
</div>

<div class="abs f-head" style="left:862px;top:4612px">Contact Info</div>
<div class="abs" style="left:862px;top:4654px;display:flex;flex-direction:column;gap:9px">
  <div class="f-item"><svg width="12" height="12" viewBox="0 0 12 12"><path d="M2 1 L4.5 1 L5.5 4 L4 5 Q5 7.5 7 8 L8 6.5 L11 7.5 L11 10 Q11 11 10 11 Q1 10 1 2 Q1 1 2 1Z" fill="var(--footer-text)"/></svg>555-310-4827</div>
  <div class="f-item"><svg width="12" height="10" viewBox="0 0 12 10"><rect x="0" y="0" width="12" height="10" fill="var(--footer-text)"/><path d="M0 0 L6 5 L12 0" stroke="var(--footer)" stroke-width="1.2" fill="none"/></svg>DanaMoreau@KeystoneRoofCo.com</div>
  <div class="f-item"><svg width="12" height="14" viewBox="0 0 12 14"><path d="M6 14 Q0 7 0 6 A6 6 0 0 1 12 6 Q12 7 6 14Z" fill="var(--footer-text)"/><circle cx="6" cy="6" r="2.2" fill="var(--footer)"/></svg>88 Alder Way, Brookfield MA 01506</div>
</div>

<div class="abs f-rule"></div>
<div class="abs copy">© Copyright 2020 - All Rights Reserved</div>

</body>
</html>
```